yourSmileCare Brookvale Business Card

Please design a two sided business card that is Elegant and Professional
Add subtle elegant patterns to suit Spot UV printing/ or raised printing

Name: Dr Marcus T. Fenwick
Qualification: BDSc (QLD)
Title: Dental Surgeon, Clinical Director
Company: yourSmileCare Brookvale
Phone: (02) 7593 2268
Address: Shop 7/18-20 Lindon Ave Brookvale 2097
email: info@yoursmilecarebrookvale.com.au
Facebook: facebook.com/yoursmilecarebrookvale

Motto:
Quality dentistry you can trust

Description of services (not compulsory):
Preventative Dentistry | General Dentistry
Cosmetic Dentistry | Teeth Whitening
Crown and Bridge | Root Canal Therapy
Veneers | Clearvono | Orthodontics
Emergency Dental Care | After Hours

Personalised Treatment Plans
Transparent Fees

Please make sure card is elegant and professional

Target Market(s)

general population, patients,
Dental sales companies, other professions

Industry/Entity Type

Dental Clinic

Contact Information for Business Card

Name: Dr Marcus T. Fenwick
Qualification: BDSc (QLD)
Phone: (02) 7593 2268
Address: Shop 7/18-20 Lindon Ave Brookvale

Motto:

Description of services (not compulsory)

Transparent Fees

Image of dental surgery optional

Please make sure card is elegant and profession

Requirements
Must have
• Logo
• Name, Title (next to name), Business
• Phone, address, facbeook
• Must have stylish design to suit SPOT UV reflective printing
Nice to have
• Subtle elegant patterns which will have Spot UV on them when printed
• Colours to match logo colour
• Description of services
Should not have
• Small fonts that are hard to read
• DO NOT PUT IMAGES OF DENTAL INSTRUMENTS OR TEETH PLEASE

```html
<!DOCTYPE html>
<html lang="en">
<head>
<meta charset="utf-8">
<title>yourSmileCare Brookvale Business Card</title>
<link rel="stylesheet" href="https://fonts.googleapis.com/css2?family=Lato:wght@400;700;900&display=swap">
<style>
  :root {
    --bg: #2a2a2a;
    --green: #7ab83a;
    --grey: #6d6e71;
    --grey-light: #a7a9ac;
    --paper: #ffffff;
    --paper-shade: #f1f1f1;
    --dark: #1d1d1d;
    --dark-2: #2b2b2b;
    --text-light: #e6e6e6;
  }
  * { box-sizing: border-box; margin: 0; padding: 0; }
  html, body { width: 1200px; height: 873px; overflow: hidden; }
  body {
    background: var(--bg);
    font-family: "Lato", Arial, sans-serif;
    position: relative;
  }
  .card {
    position: absolute;
    width: 540px;
    height: 330px;
    overflow: hidden;
    box-shadow: 0 18px 40px rgba(0,0,0,.45);
  }

  /* Front side */
  .card-front {
    left: 70px; top: 110px;
    background: linear-gradient(180deg, var(--paper) 0%, var(--paper-shade) 100%);
  }
  .front-brand {
    position: absolute; left: 40px; top: 70px; width: 215px;
    display: flex; align-items: center; gap: 8px;
  }
  .brand-dot {
    width: 14px; height: 14px; border-radius: 50%; background: var(--green); flex: none;
  }
  .brand-name {
    font-weight: 700; font-size: 19px; line-height: 1.15; color: var(--grey);
  }
  .divider {
    position: absolute; left: 272px; top: 60px; width: 1px; height: 95px;
    background: linear-gradient(180deg, transparent, var(--grey-light), transparent);
  }
  .contact-list {
    position: absolute; left: 292px; top: 62px; list-style: none;
    font-size: 13px; color: var(--grey);
  }
  .contact-list li { display: flex; align-items: center; gap: 9px; height: 27px; }
  .contact-list svg { width: 14px; height: 14px; fill: var(--green); flex: none; }
  .person {
    position: absolute; left: 40px; top: 200px;
  }
  .person-name { font-weight: 900; font-size: 19px; color: var(--green); }
  .person-qual { font-weight: 400; font-size: 12px; color: var(--grey); margin-left: 6px; }
  .person-title { font-size: 13px; color: var(--grey); margin-top: 4px; }
  .accent-band {
    position: absolute; left: 300px; right: 0; top: 176px; height: 16px;
    background: var(--green); border-radius: 16px 0 0 0;
  }
  .address {
    position: absolute; right: 28px; top: 262px;
    font-weight: 700; font-size: 13px; color: var(--green);
  }
  .base-strip {
    position: absolute; left: 0; right: 0; bottom: 0; height: 14px;
    background: linear-gradient(180deg, #dcdcdc, #c4c4c4);
  }

  /* Back side */
  .card-back {
    left: 590px; top: 433px;
    background:
      repeating-linear-gradient(90deg, rgba(255,255,255,.025) 0 2px, transparent 2px 5px),
      linear-gradient(160deg, var(--dark-2) 0%, var(--dark) 100%);
    text-align: center;
  }
  .back-brand {
    position: absolute; left: 0; right: 0; top: 110px;
    display: flex; justify-content: center; align-items: center; gap: 12px;
  }
  .back-brand .brand-dot { width: 20px; height: 20px; }
  .back-brand .brand-name { font-size: 34px; color: var(--text-light); }
  .motto {
    position: absolute; left: 0; right: 0; top: 250px;
    font-weight: 700; font-size: 13px; letter-spacing: 5px;
    color: var(--text-light); text-transform: uppercase;
  }
</style>
</head>
<body>

<section class="card card-front">
  <div class="front-brand">
    <span class="brand-dot"></span>
    <span class="brand-name">yourSmileCare Brookvale</span>
  </div>
  <div class="divider"></div>
  <ul class="contact-list">
    <li>
      <svg viewBox="0 0 24 24" aria-hidden="true"><path d="M6.6 10.8a15.1 15.1 0 0 0 6.6 6.6l2.2-2.2a1 1 0 0 1 1-.25 11.4 11.4 0 0 0 3.6.57 1 1 0 0 1 1 1V20a1 1 0 0 1-1 1A17 17 0 0 1 3 4a1 1 0 0 1 1-1h3.5a1 1 0 0 1 1 1c0 1.25.2 2.45.57 3.57a1 1 0 0 1-.25 1z"/></svg>
      (02) 7593 2268
    </li>
    <li>
      <svg viewBox="0 0 24 24" aria-hidden="true"><circle cx="12" cy="12" r="9"/></svg>
      /yoursmilecarebrookvale
    </li>
    <li>
      <svg viewBox="0 0 24 24" aria-hidden="true"><path d="M2 5h20v14H2z M2 5l10 8 10-8" /></svg>
      info@yoursmilecarebrookvale.com.au
    </li>
  </ul>
  <div class="accent-band"></div>
  <div class="person">
    <div><span class="person-name">Dr Marcus T. Fenwick</span><span class="person-qual">BDSc (QLD)</span></div>
    <div class="person-title">Dental Surgeon, Clinical Director</div>
  </div>
  <div class="address">Shop 7/18-20 Lindon Ave Brookvale 2097</div>
  <div class="base-strip"></div>
</section>

<section class="card card-back">
  <div class="back-brand">
    <span class="brand-dot"></span>
    <span class="brand-name">yourSmileCare Brookvale</span>
  </div>
  <p class="motto">Quality dentistry you can trust</p>
</section>

</body>
</html>
```